Need Help Rebranding My Food Blog

I have a Wordpress Food blog called BeetBuddies.com. Right now it has no life and is very bland. I am rebranding this site to a new named called, TheHoneyedPath.com. I would love to have a blog that is vibrant and full of life and personality.

One of my top priorities when a new visitor comes to my site is to quickly understand what the site is about (Gluten-free, dairy-free sweets that taste delicious).

I also want people to feel a connection with me when they come to the site.

Here are some other things that I'd like in the blog design...

1. Optin
My business is driven by adding people to my list so it is very important for me to have an optin front and center/ above-the-fold. See https://www.clevertidyearnings.com/ as an example. The headline that I would like is "Gluten-free & dairy-free sweets that actually taste good"

2. Vibrant/full life
The next important aspect of this blog is that it is vibrant. I like colors that remind me of a SUNSET. See attachments for logo and color scheme. Here's an example of a site I really like that is vibrant: http://www.sugarandopendays.com/

Also see Image titled: "Sample: Feeling". Notice the feeling you get from the image/brush strokes and how it feels light, breezy, and free spirited.

3. Food Images
The last important aspect for my blog is to showcase my recipes. I have attached a few of them as examples. Its really important for a food blog to showcase beautiful pictures of recipes for people to see so will definitely need this in the design.

Also, attached...
1. Image of me.
2. New logo for TheHoneyedPath (notice: don't use the one attached as "Sample/Feeling". That's just for reference of the feeling I like.)

Thanks!

Marion

P.S. I didn't include all the copy that would be needed so feel free to use the "lorem ipsum" text as placeholder if need be.

Target Market(s)

stay-at-home moms, dairy-free & gluten allergies, love desserts & sweets

Coding

Coded - Design and coding required

Font styles to use
Sans Serif

Requirements
Must have
• 1. Optin area with my picture and what I'm about ""Gluten-free & dairy-free sweets that actually taste good""
• 2. Must have personality/vibrancy to the site. Think full of life, not dull like my current website... beetbuddies.com
• 3. Highlight food images (Vertical image holders only)
Nice to have
• Color scheme should be based on my logo
Should not have
• No black or grey colors

```html
<!DOCTYPE html>
<html lang="en">
<head>
<meta charset="utf-8">
<title>TheHoneyedPath – Gluten-free &amp; dairy-free sweets</title>
<link href="https://fonts.googleapis.com/css2?family=Raleway:wght@300;400;600;700;800&family=Open+Sans:wght@400;600;700&display=swap" rel="stylesheet">
<style>
:root{
  --wine:#8c1d3f;
  --wine-deep:#6e1230;
  --wine-soft:#a3284d;
  --rose:#e3325c;
  --rose-light:#f5d3dc;
  --ink:#2a1a22;
  --body:#6f5a63;
  --muted:#a08f96;
  --rule:#eadde2;
  --paper:#ffffff;
  --night:#10283a;
}
*{box-sizing:border-box;margin:0;padding:0}
html,body{width:1200px;height:4036px;overflow:hidden}
body{position:relative;background:var(--paper);font-family:"Open Sans",sans-serif;color:var(--body)}
a{color:inherit;text-decoration:none}

/* hero */
.hero{position:absolute;left:0;top:0;width:1200px;height:705px;overflow:hidden;
  background:
   radial-gradient(circle at 590px 130px,rgba(255,255,255,.10) 0 38px,transparent 40px),
   radial-gradient(circle at 500px 60px,rgba(255,255,255,.07) 0 24px,transparent 26px),
   radial-gradient(circle at 160px 560px,rgba(255,255,255,.06) 0 46px,transparent 48px),
   radial-gradient(circle at 420px 620px,rgba(255,255,255,.07) 0 30px,transparent 32px),
   radial-gradient(circle at 700px 420px,rgba(255,255,255,.06) 0 52px,transparent 54px),
   radial-gradient(circle at 60px 300px,rgba(255,255,255,.05) 0 28px,transparent 30px),
   radial-gradient(ellipse at 40% 40%,var(--wine-soft),var(--wine) 55%,var(--wine-deep));}
.hero-photo{position:absolute;left:645px;top:54px;width:555px;height:651px;
  background:radial-gradient(ellipse at 55% 45%,#f1d9cc 0%,#e4c0b0 30%,#c98e92 60%,rgba(140,29,63,0) 80%);}
.brand{position:absolute;left:60px;top:36px;font-family:"Raleway",sans-serif;font-weight:700;font-size:26px;color:#f3b6c6;display:flex;align-items:center;gap:10px}
.brand .dot{width:12px;height:12px;border-radius:50%;background:#f3b6c6}
.nav{position:absolute;top:47px;left:0;width:1200px;height:20px;font-family:"Raleway",sans-serif;font-weight:700;font-size:13px;color:#fff;letter-spacing:.5px}
.nav a{position:absolute;top:0}
.nav svg{position:absolute;left:1117px;top:1px}
.hero h1{position:absolute;left:100px;top:216px;font-family:"Raleway",sans-serif;font-weight:400;font-size:40px;line-height:48px;color:#fff}
.hero h1 span{display:block;font-weight:300;font-size:34px}
.hero .lead{position:absolute;left:100px;top:330px;font-family:"Raleway",sans-serif;font-weight:700;font-size:24px;color:#fff}
.hero .count{position:absolute;left:100px;top:369px;font-size:16px;color:#fff}
.hero .count b{font-weight:700}
.optin input{position:absolute;left:100px;width:363px;height:35px;border:0;border-radius:3px;padding:0 12px;font:13px "Open Sans",sans-serif;color:var(--muted);background:#fff}
.optin .btn{position:absolute;left:100px;top:530px;width:115px;height:35px;border:0;border-radius:3px;background:var(--rose);color:#fff;font:700 12px "Open Sans",sans-serif;letter-spacing:.5px}
.scroll-cue{position:absolute;left:582px;top:617px}

/* dinner strip */
.section-title{position:absolute;left:0;top:746px;width:1200px;text-align:center;font-family:"Raleway",sans-serif;font-weight:800;font-size:25px;color:var(--ink)}
.dish{position:absolute;top:812px;width:323px;height:428px}
.dish .pic{height:315px}
.dish .cap{height:113px;background:var(--wine);color:#fff;text-align:center;padding-top:16px}
.dish .cap b{display:block;font-family:"Raleway",sans-serif;font-weight:800;font-size:22px;letter-spacing:.5px}
.dish .cap span{display:block;font-size:16px;line-height:24px;margin-top:6px;padding:0 30px}

/* posts */
.post{position:absolute;left:100px;width:694px}
.post h2{font-family:"Raleway",sans-serif;font-weight:800;font-size:29px;line-height:36px;color:var(--ink);text-transform:uppercase}
.meta{margin-top:14px;font-size:12px;color:var(--muted);display:flex;gap:24px}
.post .pic{height:428px;margin-top:30px}
.excerpt{margin-top:46px;font-size:13px;line-height:27px;color:var(--body)}
.taxo{font-size:12px;line-height:28px;color:var(--muted)}
.taxo b{color:var(--rose);font-weight:700}
.read{display:inline-block;margin-top:14px;width:138px;height:38px;line-height:38px;text-align:center;border-radius:3px;background:var(--rose);color:#fff;font-size:12px;font-weight:700}
.divider{position:absolute;left:100px;width:694px;height:5px;background:var(--rule)}

.pager{position:absolute;left:409px;top:3882px;display:flex;gap:8px;font-size:11px}
.pager span{height:27px;line-height:27px;padding:0 11px;background:#f6eef1;border:1px solid var(--rule);color:var(--ink)}

/* sidebar */
.side-title{position:absolute;left:842px;width:258px;font-family:"Raleway",sans-serif;font-weight:800;font-size:22px;line-height:28px;color:var(--ink);text-transform:uppercase;padding-bottom:10px;border-bottom:4px solid var(--rule)}
.tabs{position:absolute;left:842px;top:1396px;display:flex;gap:8px}
.tabs span{height:32px;line-height:32px;padding:0 14px;border-radius:3px;background:var(--rose);color:#fff;font-size:10px;font-weight:700}
.minis{position:absolute;left:842px;width:258px;list-style:none}
.minis li{display:flex;gap:16px;height:89px}
.minis .thumb{width:75px;height:75px;flex:none;border-radius:3px}
.minis b{display:block;font-size:10px;line-height:15px;font-weight:700;color:var(--ink);text-transform:uppercase;padding-top:6px}
.minis small{display:block;font-size:9px;color:var(--muted);margin-top:6px}
.cats{position:absolute;left:842px;top:2158px;width:258px;list-style:none}
.cats li{height:48px;line-height:46px;border-bottom:1px solid var(--rule);font-size:12px;color:var(--body)}
.cats li::before{content:"›";color:var(--rose);margin-right:8px}
.promo{position:absolute;left:880px;top:2596px;width:185px;height:323px;
  background:linear-gradient(180deg,#fbf3ea 0%,#f4dcc0 45%,#d9a26a 70%,#8fb26a 100%)}
.footer-brand{position:absolute;left:842px;top:3696px;width:258px;text-align:center;font-family:"Raleway",sans-serif;font-weight:700;font-size:24px;color:var(--rose)}

footer{position:absolute;left:0;top:3976px;width:1200px;height:60px;background:var(--night);color:#cfd8df;font-size:11px;text-align:center;line-height:60px}
footer a{margin:0 10px}

/* food tones */
.tone-salad{background:linear-gradient(160deg,#c97a3a,#8a4a28 50%,#e6a04a)}
.tone-beef{background:linear-gradient(160deg,#5a2a1e,#8e3b2a 50%,#3a1a14)}
.tone-noodle{background:linear-gradient(160deg,#f6efe6,#e9b86a 50%,#c6452c)}
.tone-pumpkin{background:linear-gradient(160deg,#d9c3a0,#d48a38 45%,#a85a24)}
.tone-pops{background:linear-gradient(160deg,#c9c6c0,#ef5a52 45%,#b3b0aa)}
.tone-cookie{background:linear-gradient(180deg,#fff 0%,#c9924e 40%,#8a5a2a 80%,#fff 100%)}
.tone-soup{background:linear-gradient(160deg,#f2d4a0,#c96a3a)}
.tone-green{background:linear-gradient(160deg,#a8c47a,#5a7a3a)}
.tone-bark{background:linear-gradient(160deg,#4a2a1e,#f0e6e0)}
</style>
</head>
<body>

<header class="hero">
  <div class="hero-photo" role="img" aria-label="Photo of the blog author smiling and holding a plate of cake with a fork"></div>
  <div class="brand"><span class="dot"></span>TheHoneyedPath</div>
  <nav class="nav">
    <a href="#" style="left:590px">HOME</a>
    <a href="#" style="left:718px">ABOUT</a>
    <a href="#" style="left:853px">RECIPES &#8964;</a>
    <a href="#" style="left:1000px">RESOURCES</a>
    <svg width="14" height="14" viewBox="0 0 14 14" aria-label="Search"><circle cx="6" cy="6" r="4.5" fill="none" stroke="#fff" stroke-width="1.8"/><path d="M9.5 9.5 13 13" stroke="#fff" stroke-width="1.8"/></svg>
  </nav>
  <h1>Gluten-free &amp; dairy<span>-free sweets that actually taste good</span></h1>
  <p class="lead">Let’s figure out what works!</p>
  <p class="count"><b>Join 150,000+</b> active members in the TheHoneyedPath</p>
  <form class="optin">
    <input style="top:422px" type="text" placeholder="First Name">
    <input style="top:476px" type="email" placeholder="Email Address">
    <button class="btn" type="button">SUBSCRIBE</button>
  </form>
  <svg class="scroll-cue" width="42" height="42" viewBox="0 0 42 42" aria-label="Scroll down"><circle cx="21" cy="21" r="19" fill="none" stroke="#fff" stroke-width="2"/><path d="M14 18l7 7 7-7" fill="none" stroke="#fff" stroke-width="2"/></svg>
</header>

<h2 class="section-title">MAKE THIS FOR DINNER</h2>
<div class="dish" style="left:100px"><div class="pic tone-salad" role="img" aria-label="Grilled chicken with roasted vegetables"></div><div class="cap"><b>DINNER</b><span>Winter Spa Salad with Lemon Chicken</span></div></div>
<div class="dish" style="left:438px"><div class="pic tone-beef" role="img" aria-label="Seared beef steak with rosemary"></div><div class="cap"><b>DINNER</b><span>Slow Cooker Beef Ragu with Pappardelle</span></div></div>
<div class="dish" style="left:777px"><div class="pic tone-noodle" role="img" aria-label="Spaghetti with tomato and basil"></div><div class="cap"><b>DINNER</b><span>Chipotle Sweet Potato Noodle Salad with Roasted Corn</span></div></div>

<article class="post" style="top:1290px">
  <h2>How to make pink food coloring naturally using beets</h2>
  <div class="meta"><span>by marion</span><span>2 Comments</span></div>
  <div class="pic tone-pumpkin" role="img" aria-label="Bowl of pumpkin dessert topped with pecans"></div>
  <p class="excerpt">My daughter, Lily’s favorite color is pink. Any shade of pink will do. Pale, dark or hot pink...the more pink the better. As you can imagine, Lily has been excitedly asking if it’s Valentine’s Day almost every day. Thank goodness it’s just around the corner. For us, Valentine’s Day is filled with fun heart shaped...</p>
  <p class="taxo"><b>CATEGORIES :</b> Dessert &nbsp;/&nbsp; Resources &nbsp;/&nbsp; Vegan</p>
  <p class="taxo"><b>TAGS :</b> DIY pink coloring with beets &nbsp;/&nbsp; How to make pink food coloring naturally &nbsp;/&nbsp; Natural food coloring</p>
  <a class="read" href="#">READ MORE INFO</a>
</article>
<div class="divider" style="top:2137px"></div>

<article class="post" style="top:2182px">
  <h2>Dairy-free creamy potato soup</h2>
  <div class="meta"><span>by marion</span><span>2 Comments</span></div>
  <div class="pic tone-pops" role="img" aria-label="Watermelon ice pops on a grey surface"></div>
  <p class="excerpt">My daughter, Lily’s favorite color is pink. Any shade of pink will do. Pale, dark or hot pink...the more pink the better. As you can imagine, Lily has been excitedly asking if it’s Valentine’s Day almost every day. Thank goodness it’s just around the corner. For us, Valentine’s Day is filled with fun heart shaped...</p>
  <p class="taxo"><b>CATEGORIES :</b> Dessert &nbsp;/&nbsp; Resources &nbsp;/&nbsp; Vegan</p>
  <p class="taxo"><b>TAGS :</b> DIY pink coloring with beets &nbsp;/&nbsp; How to make pink food coloring naturally &nbsp;/&nbsp; Natural food coloring</p>
  <a class="read" href="#">READ MORE INFO</a>
</article>
<div class="divider" style="top:2984px"></div>

<article class="post" style="top:3038px">
  <h2>Cinnamon swirl popcorn</h2>
  <div class="meta"><span>by marion</span><span>2 Comments</span></div>
  <div class="pic tone-cookie" role="img" aria-label="Stack of oatmeal chocolate chip cookies"></div>
  <p class="excerpt">My daughter, Lily’s favorite color is pink. Any shade of pink will do. Pale, dark or hot pink...the more pink the better. As you can imagine, Lily has been excitedly asking if it’s Valentine’s Day almost every day. Thank goodness it’s just around the corner. For us, Valentine’s Day is filled with fun heart shaped...</p>
  <p class="taxo"><b>CATEGORIES :</b> Dessert &nbsp;/&nbsp; Resources &nbsp;/&nbsp; Vegan</p>
  <p class="taxo"><b>TAGS :</b> DIY pink coloring with beets &nbsp;/&nbsp; How to make pink food coloring naturally &nbsp;/&nbsp; Natural food coloring</p>
  <a class="read" href="#">READ MORE INFO</a>
</article>

<nav class="pager"><span>Prev</span><span>1</span><span>2</span><span>3</span><span>4</span><span>5</span><span>6</span><span>...</span><span>22</span><span>Next</span></nav>

<aside>
  <h3 class="side-title" style="top:1290px">Most commented posts</h3>
  <div class="tabs"><span>RECENT POSTS</span><span>MOST COMMENTED</span></div>
  <ul class="minis" style="top:1453px">
    <li><div class="thumb tone-pumpkin" role="img" aria-label="Pumpkin dessert"></div><div><b>How to make pink food coloring naturally using beets</b><small>On 27 March 2017</small></div></li>
    <li><div class="thumb tone-bark" role="img" aria-label="Creamy potato soup"></div><div><b>Dairy-free creamy potato soup</b><small>Posted on 27 March 2017</small></div></li>
    <li><div class="thumb tone-cookie" role="img" aria-label="Cinnamon popcorn"></div><div><b>Cinnamon swirl popcorn</b><small>On 27 March 2017</small></div></li>
    <li><div class="thumb tone-soup" role="img" aria-label="Recipe collage"></div><div><b>Top 10 best recipes of 2016</b><small>Posted on 27 March 2017</small></div></li>
    <li><div class="thumb tone-soup" role="img" aria-label="Broccoli soup"></div><div><b>Cream of broccoli soup (dairy-free)</b><small>On 27 March 2017</small></div></li>
    <li><div class="thumb tone-bark" role="img" aria-label="Peppermint chocolate bark"></div><div><b>Dairy-free pretzel peppermint chocolate bark</b><small>Posted on 27 March 2017</small></div></li>
  </ul>

  <h3 class="side-title" style="top:2092px">Categories</h3>
  <ul class="cats">
    <li>Breakfast (12)</li><li>Dessert (22)</li><li>Dinner (16)</li><li>Lunch (11)</li>
    <li>Resources (14)</li><li>Snack (19)</li><li>Uncategorized (1)</li><li>Vegan (28)</li>
  </ul>

  <div class="promo" role="img" aria-label="Promotion for a vegan chickpea salad sandwich recipe"></div>

  <h3 class="side-title" style="top:2964px">Most popular</h3>
  <ul class="minis" style="top:3034px">
    <li><div class="thumb tone-pumpkin" role="img" aria-label="Pumpkin dessert"></div><div><b>How to make pink food coloring naturally using beets</b><small>On 27 March 2017</small></div></li>
    <li><div class="thumb tone-bark" role="img" aria-label="Creamy potato soup"></div><div><b>Dairy-free creamy potato soup</b><small>Posted on 27 March 2017</small></div></li>
    <li><div class="thumb tone-cookie" role="img" aria-label="Cinnamon popcorn"></div><div><b>Cinnamon swirl popcorn</b><small>On 27 March 2017</small></div></li>
    <li><div class="thumb tone-soup" role="img" aria-label="Recipe collage"></div><div><b>Top 10 best recipes of 2016</b><small>Posted on 27 March 2017</small></div></li>
    <li><div class="thumb tone-green" role="img" aria-label="Broccoli soup"></div><div><b>Cream of broccoli soup (dairy-free)</b><small>On 27 March 2017</small></div></li>
    <li><div class="thumb tone-pops" role="img" aria-label="Peppermint chocolate bark"></div><div><b>Dairy-free pretzel peppermint chocolate bark</b><small>Posted on 27 March 2017</small></div></li>
  </ul>
  <div class="footer-brand">TheHoneyedPath</div>
</aside>

<footer>Copyright © 2017. TheHoneyedPath. All rights reserved. <a href="#">Terms &amp; Conditions</a>/<a href="#">Privacy Policy</a>/<a href="#">Disclaimer</a>/<a href="#">Sitemap</a></footer>

</body>
</html>
```